verdant terraces simple classy business card design

my name is owen harlow and I run a gardening business aimed at high class verdant terraces. the business name is verdant terraces and our logo was designed on pixel forum .My clientel are anything from residential homes to businesses. I take pride in my work and know that I offer a service like no other in my area.
The business card will be used to represent my business and I want it to be not only rememberable, but simplistic and modern. Eye catching too. Of course I would like it relatable to gardening and appealing to the correct clientel - those being garden enthusiasts, prestigious homes and businesses that are after top of the line gardening services like no other on the market.
I am not a typical lawn mowing business so I don't want a typical card design that represents that. The gardens I work with are generally million dollar properties with owners who are very garden proud looking for upkeep and guidance from me along with sometimes whole new garden designs. I want the business cards to show to my clients that I take pride, as they do, in their garden. And I want them to know from my card that I am a professional, qualified horticulturist offering them a top of the line service for life. I want them to refer my business on. I want them to look at my business card and see class and professionalism in a modern unique bold way.
The card should be simple with the possibility of the logo on the front being embossed/debossed and my details on the back the card should have a organic garden feel it's very important to me that it is absolutely perfect
I am also very open to ideas and suggestions so look forward to seeing the designs. the business logo has been supplied with this project and I want the card to be double sided

Contact info is
Owen Harlow - Managing Director / Horticulturist
Phone : 0481 526 704
Email: owenharlow@verdantterraces.com.au

Target Market(s)

high class gardens residential and commercial

Industry/Entity Type

Gardener

Contact Information for Business Card

Contact info is
Phone : 0481 526 704

PLEASE MAKE CARD DOUBLE SIDED

Requirements
Must have
• organic simple classy modern feel
• must flow with the current logo that has been supplied with this project
• Double sided
• Must explain in a simple way that I deal with high end gardens and I'm a qualified horticulturist
Nice to have
• embossed debossed logo
Should not have
• shouldn't be to busy or cheap looking

```html
<!DOCTYPE html>
<html lang="en">
<head>
<meta charset="utf-8">
<title>Verdant Terraces – Business Card</title>
<link rel="stylesheet" href="https://fonts.googleapis.com/css2?family=Arimo:wght@400;700&display=swap">
<style>
  :root {
    --backdrop: #3a3431;
    --card: #1c1c1d;
    --card-edge: #111112;
    --emboss: #4a4a4c;
    --emboss-text: #6b6b6e;
    --leaf: #5aa83a;
    --ink: #f2f2f2;
    --muted: #d8d8d8;
    --divider: #6a6a6a;
  }
  * { box-sizing: border-box; margin: 0; padding: 0; }
  html, body { width: 1200px; height: 864px; overflow: hidden; }
  body {
    background: var(--backdrop);
    font-family: "Arimo", Arial, sans-serif;
    display: flex;
    flex-direction: column;
    align-items: center;
    justify-content: center;
    gap: 40px;
  }
  .card {
    width: 620px;
    height: 379px;
    background: var(--card);
    border: 1px solid var(--card-edge);
    position: relative;
  }

  /* Front */
  .card--front {
    display: flex;
    flex-direction: column;
    align-items: center;
    justify-content: center;
    gap: 34px;
  }
  .brand {
    display: flex;
    align-items: center;
    gap: 14px;
  }
  .brand__dot {
    width: 30px;
    height: 30px;
    border-radius: 50%;
  }
  .brand__name {
    font-weight: 700;
    text-transform: uppercase;
    letter-spacing: 3px;
    line-height: 1;
  }
  .card--front .brand__dot { background: var(--emboss); }
  .card--front .brand__name { color: var(--emboss-text); font-size: 34px; }
  .website {
    color: var(--emboss-text);
    font-size: 15px;
    letter-spacing: 3px;
  }

  /* Back */
  .card--back {
    display: flex;
    align-items: center;
    padding: 0 40px 0 38px;
  }
  .card--back .brand { width: 240px; gap: 10px; }
  .card--back .brand__dot { background: var(--leaf); width: 24px; height: 24px; flex: none; }
  .card--back .brand__name { color: var(--leaf); font-size: 22px; letter-spacing: 2px; line-height: 1.2; }
  .divider {
    width: 1px;
    height: 170px;
    background: var(--divider);
    margin: 0 26px 0 18px;
  }
  .details { color: var(--ink); }
  .details__name {
    color: var(--leaf);
    font-weight: 700;
    font-size: 20px;
    margin-bottom: 4px;
  }
  .details__role {
    font-size: 17px;
    margin-bottom: 16px;
  }
  .contact { list-style: none; display: flex; flex-direction: column; gap: 6px; }
  .contact__item {
    display: flex;
    align-items: center;
    gap: 9px;
    font-size: 15px;
    color: var(--muted);
  }
  .contact__icon { width: 15px; height: 15px; flex: none; }
</style>
</head>
<body>
  <section class="card card--front" aria-label="Card front">
    <div class="brand">
      <span class="brand__dot"></span>
      <span class="brand__name">Verdant Terraces</span>
    </div>
    <p class="website">www.verdantterraces.com.au</p>
  </section>

  <section class="card card--back" aria-label="Card back">
    <div class="brand">
      <span class="brand__dot"></span>
      <span class="brand__name">Verdant Terraces</span>
    </div>
    <span class="divider"></span>
    <div class="details">
      <h1 class="details__name">Owen Harlow</h1>
      <p class="details__role">Managing Director / Horticulturist</p>
      <ul class="contact">
        <li class="contact__item">
          <svg class="contact__icon" viewBox="0 0 16 16" aria-hidden="true">
            <circle cx="8" cy="8" r="8" fill="#5aa83a"/>
            <path d="M5 4.2h1.6l.8 2-1 .8a5 5 0 0 0 2.6 2.6l.8-1 2 .8v1.6c0 .5-.4.8-.9.8A7 7 0 0 1 4.2 5.1c0-.5.3-.9.8-.9z" fill="#1c1c1d"/>
          </svg>
          0481 526 704
        </li>
        <li class="contact__item">
          <svg class="contact__icon" viewBox="0 0 16 16" aria-hidden="true">
            <circle cx="8" cy="8" r="8" fill="#5aa83a"/>
            <rect x="3.8" y="5" width="8.4" height="6" rx=".6" fill="#1c1c1d"/>
            <path d="M4 5.4 8 8.4l4-3" stroke="#5aa83a" stroke-width=".9" fill="none"/>
          </svg>
          owenharlow@verdantterraces.com.au
        </li>
        <li class="contact__item">
          <svg class="contact__icon" viewBox="0 0 16 16" aria-hidden="true">
            <circle cx="8" cy="8" r="8" fill="#5aa83a"/>
            <circle cx="8" cy="8" r="4.2" fill="none" stroke="#1c1c1d" stroke-width="1"/>
            <path d="M3.8 8h8.4M8 3.8c-2 2.6-2 5.8 0 8.4M8 3.8c2 2.6 2 5.8 0 8.4" stroke="#1c1c1d" stroke-width=".8" fill="none"/>
          </svg>
          verdantterraces.com.au
        </li>
      </ul>
    </div>
  </section>
</body>
</html>
```